IT COMPANYcutting edge tec business card

we are IT company that building any apps.
we need business card in japanese and english
You don’t have to include all information in front one you can attach part of that information to back-side
company name : 株式会社ひかりの丘 (BRIGHTHILL Inc.)
concept : cutting-edge technology
role : 取締役 (director)
name : 呉 炫秀 (Oh Hyeonsuk)
post number : 154-0038
address : 東京都世田谷区西若葉台5-14-8 (5-14-8, Nishiwakabadai, Setagaya Ku, Tokyo To, 154-0038, Japan)
Tel:+81-3-5917-2846
Mobile:+81-80-7253-3169
Email : hoh@brighthill-lab.com
website : www.brighthill-lab.com

we dont have logo so please make it as well
we also looking for designer who can make homapage design.

Contact Information for Business Card

cutting-edge design and modern for IT

Font styles to use
Sans Serif

Colors
34a6d7
33b8a4
6092c4
3377b5
886aae
6b449b
b868aa
a64599

Requirements
Must have
• Simple but designed

```html
<!DOCTYPE html>
<html lang="ja">
<head>
<meta charset="utf-8">
<title>株式会社ひかりの丘 — Business Card</title>
<link rel="stylesheet" href="https://fonts.googleapis.com/css2?family=Montserrat:wght@400;500&family=Noto+Sans+JP:wght@400;500;700&display=swap">
<style>
  :root {
    --stage: #eceded;
    --paper: #ffffff;
    --charcoal: #4a4849;
    --ink: #2f2e2f;
    --muted: #7a7879;
    --sky: #34a6d7;
    --teal: #33b8a4;
    --blue: #3377b5;
    --violet: #6b449b;
    --magenta: #a64599;
    --on-dark: #f2f2f2;
    --on-dark-dim: #d4d3d3;
    --rule: #8e8c8d;
  }
  * { margin: 0; padding: 0; box-sizing: border-box; }
  html, body {
    width: 678px; height: 1200px; overflow: hidden;
    background: var(--stage);
    font-family: "Noto Sans JP", "Montserrat", sans-serif;
  }
  .sheet {
    width: 678px; height: 1200px;
    display: flex; justify-content: center; align-items: center; gap: 40px;
  }
  .card {
    position: relative; width: 290px; height: 522px; overflow: hidden;
    box-shadow: 0 10px 22px rgba(0,0,0,.14);
  }

  /* Brand lockup */
  .brand { position: absolute; display: flex; align-items: center; }
  .brand__dot { border-radius: 50%; background: var(--blue); flex: none; }
  .brand__name { font-weight: 500; color: var(--ink); line-height: 1.25; }

  /* Front */
  .card--front { background: var(--paper); }
  .card--front .brand { left: 18px; top: 36px; gap: 9px; }
  .card--front .brand__dot { width: 32px; height: 32px; }
  .card--front .brand__name { font-size: 11px; }

  .person { position: absolute; left: 24px; top: 200px; }
  .person__role { font-size: 10.5px; color: var(--blue); letter-spacing: .5px; margin-bottom: 8px; }
  .person__role span { font-family: "Montserrat", sans-serif; margin-left: 6px; }
  .person__name { font-size: 27px; font-weight: 700; color: var(--ink); letter-spacing: 3px; line-height: 1; }
  .person__latin { font-family: "Montserrat", sans-serif; font-size: 11.5px; color: var(--ink); margin-top: 6px; }
  .postcode {
    position: absolute; left: 24px; top: 296px;
    font-family: "Montserrat", sans-serif; font-size: 11.5px; color: var(--blue);
  }
  .accent-block {
    position: absolute; right: 14px; top: 294px; width: 32px; height: 32px;
    background: linear-gradient(135deg, var(--sky), var(--violet));
  }
  .contact {
    position: absolute; left: 0; right: 0; bottom: 0; height: 196px;
    background: var(--charcoal); color: var(--on-dark);
    padding: 20px 18px 0 30px;
  }
  .contact__row { display: flex; align-items: center; gap: 9px; height: 23px; font-family: "Montserrat", sans-serif; font-size: 12px; }
  .contact__label { font-size: 9px; color: var(--on-dark-dim); width: 16px; }
  .icon { width: 14px; height: 14px; flex: none; }
  .contact__rule { height: 1px; background: var(--rule); margin: 8px 0 10px -12px; }
  .address { display: flex; gap: 9px; }
  .address__ja { font-size: 12px; line-height: 1.2; }
  .address__en { font-family: "Montserrat", sans-serif; font-size: 8px; line-height: 1.35; margin-top: 3px; color: var(--on-dark-dim); }

  /* Back */
  .card--back { background: var(--charcoal); }
  .card--back .brand {
    left: 0; right: 0; top: 186px; flex-direction: column; gap: 16px; text-align: center;
  }
  .card--back .brand__dot { width: 46px; height: 46px; background: var(--sky); }
  .card--back .brand__name { font-size: 16px; color: var(--on-dark); letter-spacing: .5px; }
  .back__band {
    position: absolute; left: 26px; right: 26px; top: 452px; height: 3px;
    background: linear-gradient(90deg, var(--sky), var(--teal), var(--blue), var(--violet), var(--magenta));
  }
  .back__url {
    position: absolute; left: 0; right: 0; top: 476px; text-align: center;
    font-family: "Montserrat", sans-serif; font-size: 11px; letter-spacing: 3.2px; color: var(--on-dark);
  }
</style>
</head>
<body>
<main class="sheet">
  <section class="card card--front" aria-label="Business card front">
    <div class="brand">
      <span class="brand__dot"></span>
      <p class="brand__name">株式会社ひかりの丘<br>BRIGHTHILL Inc.</p>
    </div>
    <div class="person">
      <p class="person__role">取締役<span>Director</span></p>
      <p class="person__name">呉 炫秀</p>
      <p class="person__latin">Oh Hyeonsuk</p>
    </div>
    <p class="postcode">Post Number : 154-0038</p>
    <div class="accent-block" role="img" aria-label="Small blue-to-violet accent square"></div>

    <div class="contact">
      <p class="contact__row">
        <svg class="icon" viewBox="0 0 14 14" fill="none" stroke="currentColor" stroke-width="1.1"><path d="M3.2 1.2 L5.4 1.2 L6.2 4.2 L4.8 5.2 C5.6 7 7 8.4 8.8 9.2 L9.8 7.8 L12.8 8.6 L12.8 10.8 C12.8 12 11.8 12.8 10.6 12.8 C5.6 12.4 1.6 8.4 1.2 3.4 C1.2 2.2 2 1.2 3.2 1.2Z"/></svg>
        +81-3-5917-2846
      </p>
      <p class="contact__row">
        <svg class="icon" viewBox="0 0 14 14" fill="none" stroke="currentColor" stroke-width="1.1"><rect x="3.5" y="0.8" width="7" height="12.4" rx="1.2"/><line x1="6" y1="11" x2="8" y2="11"/></svg>
        +81-80-7253-3169
      </p>
      <p class="contact__row">
        <svg class="icon" viewBox="0 0 14 14" fill="none" stroke="currentColor" stroke-width="1.1"><rect x="0.8" y="2.8" width="12.4" height="8.4"/><polyline points="0.8,2.8 7,8 13.2,2.8"/></svg>
        hoh@brighthill-lab.com
      </p>
      <p class="contact__row">
        <svg class="icon" viewBox="0 0 14 14" fill="none" stroke="currentColor" stroke-width="1.1"><circle cx="7" cy="7" r="4.6"/><ellipse cx="7" cy="7.4" rx="6.6" ry="2.2" transform="rotate(-12 7 7)"/></svg>
        www.brighthill-lab.com
      </p>
      <div class="contact__rule"></div>
      <div class="address">
        <svg class="icon" viewBox="0 0 14 14" fill="none" stroke="currentColor" stroke-width="1.1"><path d="M7 13.2 C4 9.6 2.4 7.4 2.4 5.2 A4.6 4.6 0 0 1 11.6 5.2 C11.6 7.4 10 9.6 7 13.2Z"/><circle cx="7" cy="5.2" r="1.6"/></svg>
        <div>
          <p class="address__ja">東京都世田谷区西若葉台5-14-8</p>
          <p class="address__en">(5-14-8, Nishiwakabadai, Setagaya Ku,<br>Tokyo To, 154-0038, Japan</p>
        </div>
      </div>
    </div>
  </section>

  <section class="card card--back" aria-label="Business card back">
    <div class="brand">
      <span class="brand__dot"></span>
      <p class="brand__name">株式会社ひかりの丘<br>BRIGHTHILL Inc.</p>
    </div>
    <div class="back__band"></div>
    <p class="back__url">www.brighthill-lab.com</p>
  </section>
</main>
</body>
</html>
```